Voyage Wellcare Hub Business Cards

We need business cards for our new start-up online travel health clinic. Visit our website voyagewellcarehub.ca for branding and more info.

Target Market(s)

Travellers

Industry/Entity Type

Business

Contact Information for Business Card

Maya Koslowski
maya@voyagewellcarehub.ca
+1 555 283 6194
voyagewellcarehub.ca

Font styles to use
Sans Serif

Colors
f68d4d

```html
<!DOCTYPE html>
<html lang="en">
<head>
<meta charset="utf-8">
<title>Voyage Wellcare Hub – Business Cards</title>
<link rel="stylesheet" href="https://fonts.googleapis.com/css2?family=Arimo:wght@400;700&family=Noto+Sans:ital,wght@0,400;1,400&display=swap">
<style>
  :root {
    --brand-orange: #f68d4d;
    --card-white: #ffffff;
    --text-grey: #a3a3a3;
    --backdrop: #2a2a2a;
    --tagline-light: #fde9dc;
  }
  * { box-sizing: border-box; margin: 0; padding: 0; }
  html, body { width: 1189px; height: 1200px; overflow: hidden; }
  body {
    background: var(--backdrop);
    position: relative;
    font-family: "Arimo", Arial, sans-serif;
  }
  .card {
    position: absolute;
    left: 171px;
    width: 856px;
    height: 489px;
    border-radius: 30px;
    box-shadow: 0 6px 18px rgba(0,0,0,0.45);
  }
  .card--front { top: 66px; background: var(--brand-orange); }
  .card--back { top: 625px; background: var(--card-white); }

  .brand-name {
    position: absolute;
    font-family: "Noto Sans", Verdana, sans-serif;
    font-weight: 400;
    white-space: nowrap;
    letter-spacing: -0.01em;
  }
  .tagline {
    position: absolute;
    font-family: "Noto Sans", Verdana, sans-serif;
    font-style: italic;
    white-space: nowrap;
  }

  .card--front .brand-name {
    left: 0; right: 0; top: 208px;
    text-align: center;
    font-size: 50px;
    color: var(--card-white);
  }
  .card--front .tagline {
    right: 150px; top: 278px;
    font-size: 21px;
    color: var(--card-white);
  }
  .front-url {
    position: absolute;
    left: 0; right: 0; top: 407px;
    text-align: center;
    font-size: 18px;
    letter-spacing: 0.42em;
    color: var(--card-white);
  }

  .card--back .brand-name {
    left: 60px; top: 224px;
    font-size: 32px;
    color: var(--brand-orange);
  }
  .card--back .tagline {
    left: 199px; top: 266px;
    font-size: 13px;
    color: var(--text-grey);
  }
  .divider {
    position: absolute;
    left: 437px; top: 179px;
    width: 2px; height: 132px;
    background: var(--brand-orange);
  }
  .contact-name {
    position: absolute;
    left: 476px; top: 175px;
    font-size: 30px;
    font-weight: 700;
    color: var(--brand-orange);
  }
  .contact-list {
    position: absolute;
    left: 476px; top: 229px;
    list-style: none;
  }
  .contact-item {
    display: flex;
    align-items: center;
    height: 29px;
    font-size: 21px;
    color: var(--text-grey);
  }
  .contact-icon {
    width: 25px; height: 25px;
    margin-right: 11px;
    flex: none;
  }
</style>
</head>
<body>
  <section class="card card--front">
    <p class="brand-name">Voyage Wellcare Hub</p>
    <p class="tagline">Online Travel Health Experts</p>
    <p class="front-url">voyagewellcarehub.ca</p>
  </section>

  <section class="card card--back">
    <p class="brand-name">Voyage Wellcare Hub</p>
    <p class="tagline">Online Travel Health Experts</p>
    <div class="divider"></div>
    <h1 class="contact-name">Maya Koslowski</h1>
    <ul class="contact-list">
      <li class="contact-item">
        <svg class="contact-icon" viewBox="0 0 25 25" aria-hidden="true">
          <circle cx="12.5" cy="12.5" r="11.5" fill="none" stroke="#f68d4d" stroke-width="1.5"/>
          <path d="M6.5 10.5c0-2 2.5-3 6-3s6 1 6 3v1h-3v-1.5h-6v1.5h-3z" fill="#f68d4d"/>
          <rect x="8" y="12" width="9" height="5.5" rx="1" fill="#f68d4d"/>
        </svg>
        +1 555 283 6194
      </li>
      <li class="contact-item">
        <svg class="contact-icon" viewBox="0 0 25 25" aria-hidden="true">
          <circle cx="12.5" cy="12.5" r="11.5" fill="none" stroke="#f68d4d" stroke-width="1.5"/>
          <rect x="6.5" y="8.5" width="12" height="8" fill="#f68d4d"/>
          <path d="M6.5 8.5l6 5 6-5M6.5 16.5l4.5-4M18.5 16.5l-4.5-4" fill="none" stroke="#fff" stroke-width="1"/>
        </svg>
        maya@voyagewellcarehub.ca
      </li>
      <li class="contact-item">
        <svg class="contact-icon" viewBox="0 0 25 25" aria-hidden="true">
          <circle cx="12.5" cy="12.5" r="11.5" fill="none" stroke="#f68d4d" stroke-width="1.5"/>
          <g fill="none" stroke="#f68d4d" stroke-width="1.1">
            <circle cx="12.5" cy="12.5" r="6.5"/>
            <ellipse cx="12.5" cy="12.5" rx="3" ry="6.5"/>
            <path d="M6 12.5h13M7 9h11M7 16h11"/>
          </g>
        </svg>
        voyagewellcarehub.ca
      </li>
    </ul>
  </section>
</body>
</html>
```